July 4th Postcard to existing clients

5x7 postcard wishing our clients happy 4th of July. Card should read on the back "Thank You For Being A Valued Client!. Stay Safe And Enjoy Your Independence Day Celebrations!"

Patriotic theme with fireworks is ideal. We are a law firm so should still have a feel of professionalism while still being fun since it is for a fun holiday.

```html
<!DOCTYPE html>
<html lang="en">
<head>
<meta charset="utf-8">
<title>Harwell Law – Independence Day Postcard</title>
<link rel="stylesheet" href="https://fonts.googleapis.com/css2?family=Oswald:wght@400;500;700&family=Lato:wght@400;700&family=Montserrat:wght@300;400&display=swap">
<style>
  :root{
    --navy:#1f4a8a;
    --panel:#264b84;
    --red:#d0112b;
    --ink:#1a1a1a;
    --grey:#6a6a6a;
    --stamp:#c8c8c8;
    --white:#ffffff;
  }
  *{margin:0;padding:0;box-sizing:border-box}
  html,body{width:960px;height:1200px;overflow:hidden;background:var(--white)}
  .canvas{position:relative;width:960px;height:1200px}
  .card{position:absolute;width:733px;height:524px;background:var(--white);box-shadow:2px 3px 8px rgba(0,0,0,.35);overflow:hidden}
  .card--front{left:112px;top:42px}
  .card--back{left:114px;top:630px}
  .card svg.shapes{position:absolute;left:0;top:0}
  .brand{position:absolute;display:flex;align-items:center;gap:10px;font-family:'Montserrat',sans-serif;font-weight:300;font-size:31px;letter-spacing:1px;color:var(--grey);white-space:nowrap}
  .brand-square{width:22px;height:22px;background:#9ea3c4}
  .front .brand{left:40px;top:92px}
  .headline{position:absolute;left:22px;top:130px;font-family:'Oswald',sans-serif;font-weight:700;font-size:47px;color:var(--navy);line-height:1}
  .headline-accent{position:absolute;left:22px;top:186px;font-family:'Oswald',sans-serif;font-weight:400;font-size:45px;color:var(--red);line-height:1;letter-spacing:.5px}
  .beliefs{position:absolute;left:22px;top:248px;width:420px;font-family:'Lato',sans-serif;font-size:11.6px;line-height:14px;color:var(--ink)}
  .beliefs p{margin-bottom:8px}
  .beliefs p:last-child{margin-top:13px}
  .beliefs strong{color:var(--red);font-weight:700}
  .call{position:absolute;font-family:'Oswald',sans-serif;font-weight:700;white-space:nowrap;line-height:1}
  .front .call{left:22px;top:438px;font-size:38px;color:var(--ink)}
  .front .call .label{color:var(--navy)}
  .web-strip{position:absolute;left:26px;top:500px;font-family:'Lato',sans-serif;font-size:12px;letter-spacing:8.4px;color:var(--white)}
  .back .brand{left:72px;top:84px}
  .thanks{position:absolute;left:32px;top:116px;font-family:'Oswald',sans-serif;font-weight:700;font-size:66px;color:var(--red);line-height:1}
  .valued{position:absolute;left:32px;top:186px;font-family:'Oswald',sans-serif;font-weight:500;font-size:27px;color:var(--navy);line-height:1}
  .wish{position:absolute;left:32px;top:218px;font-family:'Lato',sans-serif;color:var(--ink);line-height:1.15}
  .wish .line1{font-size:25px}
  .wish .line2{font-size:19.5px}
  .back .call{left:26px;top:280px;font-size:33px;color:var(--white)}
  .contact{position:absolute;left:0;top:322px;width:300px;text-align:center;font-family:'Lato',sans-serif;font-size:12px;line-height:15px;color:var(--white)}
  .contact p{margin-bottom:4px}
  .contact p.address{margin-bottom:8px}
  .contact strong{font-weight:700}
  .stamp{position:absolute;left:641px;top:20px;width:70px;height:86px;background:var(--stamp)}
</style>
</head>
<body>
<main class="canvas">

  <section class="card card--front front">
    <svg class="shapes" width="733" height="524" viewBox="0 0 733 524">
      <defs>
        <linearGradient id="flagWash" x1="0" y1="0" x2="1" y2="1">
          <stop offset="0" stop-color="#ffffff"/>
          <stop offset=".55" stop-color="#f3eef1"/>
          <stop offset="1" stop-color="#dfe3ee"/>
        </linearGradient>
        <linearGradient id="justicePhoto" x1="0" y1="0" x2="1" y2="1">
          <stop offset="0" stop-color="#1a1714"/>
          <stop offset=".5" stop-color="#5a5248"/>
          <stop offset="1" stop-color="#2b2620"/>
        </linearGradient>
        <linearGradient id="speakerPhoto" x1="0" y1="0" x2="0" y2="1">
          <stop offset="0" stop-color="#c9b9b6"/>
          <stop offset=".45" stop-color="#4a5677"/>
          <stop offset="1" stop-color="#1d2438"/>
        </linearGradient>
      </defs>
      <rect width="733" height="524" fill="url(#flagWash)"/>
      <polygon points="308,0 733,0 733,294 484,334" fill="url(#justicePhoto)" role="img" aria-label="Gavel, open law book and statue of Lady Justice on a dark background"/>
      <polygon points="478,352 733,312 733,524 472,524" fill="url(#speakerPhoto)" role="img" aria-label="Attorney in a suit speaking at a microphone before an American flag"/>
      <polyline points="286,0 474,348 733,308" fill="none" stroke="var(--navy)" stroke-width="7"/>
      <polyline points="299,0 481,340 733,300" fill="none" stroke="var(--red)" stroke-width="5"/>
      <polygon points="0,492 412,492 436,524 0,524" fill="#111111"/>
    </svg>

    <div class="brand"><span class="brand-square"></span>HARWELL LAW</div>
    <h1 class="headline">It’s about taking</h1>
    <h2 class="headline-accent">RESPONSSIBILITY</h2>
    <div class="beliefs">
      <p><strong>We Believe</strong> in personal responsibility. We believe that others should be held accountable when their behavior leads to injury or loss of life.</p>
      <p><strong>We Believe</strong> that accident victims deserve the same quality of legal representation as insurance companies and large wealthy corporations.</p>
      <p><strong>We Believe</strong> that drunk and drugged drivers must be held accountable for the damage they inflict.</p>
      <p><strong>We Believe</strong> in every citizen’s right to equal justice and protection of the law regardless of race, creed or social condition.</p>
      <p><strong>We Believe</strong> that by diligently representing our clients, and working to prevent accidents from occurring, we can leave the world a little safer than we found it.</p>
    </div>
    <div class="call"><span class="label">Call Us:</span> 417-555-0142</div>
    <div class="web-strip">www.harwelllaw.com</div>
  </section>

  <section class="card card--back back">
    <svg class="shapes" width="733" height="524" viewBox="0 0 733 524">
      <defs>
        <linearGradient id="backWash" x1="0" y1="0" x2="1" y2="1">
          <stop offset="0" stop-color="#ffffff"/>
          <stop offset=".6" stop-color="#f4eef0"/>
          <stop offset="1" stop-color="#e8e2e8"/>
        </linearGradient>
      </defs>
      <polygon points="0,0 388,0 302,440 0,458" fill="url(#backWash)"/>
      <polygon points="0,277 327,277 320,316 0,316" fill="#111111"/>
      <polygon points="0,316 320,316 297,436 0,452" fill="var(--panel)"/>
      <polyline points="390,0 302,441 0,459" fill="none" stroke="var(--red)" stroke-width="6"/>
      <polyline points="411,0 318,451 0,473" fill="none" stroke="var(--navy)" stroke-width="7"/>
    </svg>

    <div class="brand"><span class="brand-square"></span>HARWELL LAW</div>
    <h1 class="thanks">Thank You</h1>
    <h2 class="valued">For Being A Valued Client!</h2>
    <div class="wish">
      <div class="line1">Stay Safe And Enjoy Your</div>
      <div class="line2">Independence Day Celebrations!</div>
    </div>
    <div class="call">Call Us: 417-555-0142</div>
    <div class="contact">
      <p class="address">1480 West Maple Crest Avenue<br>Fairview, Missouri 65810</p>
      <p><strong>Telephone:</strong> (417) 555-0142</p>
      <p><strong>Toll Free:</strong> 1-800-555-0199</p>
      <p><strong>Fax:</strong> (417) 555-0177</p>
      <p>www.harwelllaw.com</p>
    </div>
    <div class="stamp"></div>
  </section>

</main>
</body>
</html>
```